Brisk Ledger Hub's Facebook Cover Design

I am in need of a social media cover for my company's Facebook account. Please leverage the green logos and color palette attached.

Brisk Ledger Hub offers 2 primary services:
1.) Business Automation Services
2.) AI (artificial intelligence integrations)

While a lot of what we do is highly technical, what we deliver is not. In a nutshell, we help our clients to connect their data regardless of what application that data is sitting in. Because we can connect that data, often times we can:

A.) offer more intelligent marketing and help our client increase their revenue.
B.) automate highly repetitive tasks using technology and drive down their costs thus saving them money
C.) help our clients use AI to better serve their customers

You can read a little bit about our company here: https://www.briskledgerhub.example

Our tagline is: "Connect data to increase the flow of profitability."

Visually, we'd like your help to illustrate the "connecting" of these applications. Please let me know if you have any questions.

Target Market(s)

Business Owners or Marketing Managers

Industry/Entity Type

Marketing technologies.

Font styles to use
Sans Serif

Requirements
Must have
• Please make every effort to have the cover compatible with the color palette of the attached images.
Should not have
• Please do not use the standard clipart or stock libraries of AI = robot. If you do, please make them small. We help business glue their data from different sources to solve real work problems. Little robots are overused.

```html
<!DOCTYPE html>
<html lang="en">
<head>
<meta charset="utf-8">
<title>Brisk Ledger Hub – Facebook Cover</title>
<link rel="stylesheet" href="https://fonts.googleapis.com/css2?family=Poppins:wght@300;500;600;700&display=swap">
<style>
  :root {
    --page-bg: #f3fde6;
    --green-deep: #071a07;
    --green-dark: #0f4a12;
    --green-mid: #157a1a;
    --green-bright: #2bc62f;
    --accent-lime: #8dc95a;
    --check-green: #1d6b1f;
    --white: #ffffff;
  }
  * { box-sizing: border-box; margin: 0; padding: 0; }
  html, body {
    width: 1200px;
    height: 1200px;
    overflow: hidden;
    background: var(--page-bg);
    font-family: "Poppins", sans-serif;
  }
  .cover {
    position: absolute;
    left: 89px;
    top: 396px;
    width: 1021px;
    height: 378px;
    overflow: hidden;
    color: var(--white);
  }
  .cover-backdrop {
    position: absolute;
    inset: 0;
    background:
      radial-gradient(ellipse 45% 60% at 78% 85%, rgba(43,198,47,0.85), rgba(43,198,47,0) 70%),
      linear-gradient(100deg, var(--green-deep) 0%, var(--green-dark) 35%, var(--green-mid) 65%, var(--green-bright) 100%);
  }
  .brand-name {
    position: absolute;
    right: 41px;
    top: 44px;
    font-size: 28px;
    font-weight: 700;
    letter-spacing: -0.5px;
    line-height: 1;
    color: var(--white);
  }
  .tagline {
    position: absolute;
    left: 46px;
    top: 88px;
    font-size: 64px;
    font-weight: 300;
    line-height: 56px;
    letter-spacing: -0.5px;
  }
  .tagline span { display: block; white-space: nowrap; }
  .tagline .highlight {
    font-weight: 700;
    color: var(--accent-lime);
    letter-spacing: -1.5px;
  }
  .benefits {
    position: absolute;
    top: 328px;
    left: 47px;
    list-style: none;
  }
  .benefit {
    position: absolute;
    top: 0;
    display: flex;
    align-items: center;
    gap: 14px;
    font-size: 22px;
    font-weight: 500;
    white-space: nowrap;
    line-height: 34px;
  }
  .benefit svg { width: 34px; height: 34px; flex: none; }
  .benefit:nth-child(1) { left: 0; }
  .benefit:nth-child(2) { left: 331px; }
  .benefit:nth-child(3) { left: 600px; }
</style>
</head>
<body>
  <section class="cover">
    <div class="cover-backdrop" role="img" aria-label="Green gradient backdrop with a woven data-line pattern and a flowing curved shape"></div>

    <div class="brand-name">Brisk Ledger Hub</div>

    <h1 class="tagline">
      <span>Connect data to</span>
      <span>increase the flow of</span>
      <span class="highlight">profitability.</span>
    </h1>

    <ul class="benefits">
      <li class="benefit">
        <svg viewBox="0 0 34 34" aria-hidden="true"><circle cx="17" cy="17" r="17" fill="#fff"/><path d="M10 17.5l5 5 9-10" fill="none" stroke="#0b2a0b" stroke-width="4" stroke-linecap="round" stroke-linejoin="round"/></svg>
        Grow your revenue
      </li>
      <li class="benefit">
        <svg viewBox="0 0 34 34" aria-hidden="true"><circle cx="17" cy="17" r="17" fill="#fff"/><path d="M10 17.5l5 5 9-10" fill="none" stroke="#124a14" stroke-width="4" stroke-linecap="round" stroke-linejoin="round"/></svg>
        Reduce costs
      </li>
      <li class="benefit">
        <svg viewBox="0 0 34 34" aria-hidden="true"><circle cx="17" cy="17" r="17" fill="#fff"/><path d="M10 17.5l5 5 9-10" fill="none" stroke="#2aa02e" stroke-width="4" stroke-linecap="round" stroke-linejoin="round"/></svg>
        Increase data accuracy
      </li>
    </ul>
  </section>
</body>
</html>
```